QRV In Home Flier

To prepare a flier to be placed directly into existing clients homes, which shares additional services available. These are clients that are using QRV Cleaning services and we want to use our QRV Pest Control or BWO (Bondo Mend Up)Maintenance Services

Target Market(s)

residential home owners / Renters

Industry/Entity Type

Property Maintenance

Colors

Designer to choose colors to be used in the design.

Requirements
Must have
• Must be crisp and clean - design should pop - A CLEAR call to action
Nice to have
• See previous designed uploaded
Should not have

```html
<!DOCTYPE html>
<html lang="en">
<head>
<meta charset="utf-8">
<title>QRV In Home Fliers</title>
<link href="https://fonts.googleapis.com/css2?family=Montserrat:wght@500;700;800;900&family=Raleway:wght@400;500;600;700&display=swap" rel="stylesheet">
<style>
  :root {
    --stage: #9c9c9c;
    --orange: #e98a1b;
    --navy: #263d8c;
    --navy-deep: #1f3278;
    --ink: #2b2b2b;
    --panel: #f0f0f0;
    --band: rgba(40, 40, 40, 0.82);
    --white: #ffffff;
  }
  * { box-sizing: border-box; margin: 0; padding: 0; }
  html, body { width: 1200px; height: 858px; overflow: hidden; }
  body { background: var(--stage); font-family: "Raleway", Arial, sans-serif; position: relative; }

  .flier {
    position: absolute; top: 36px; width: 524px; height: 740px;
    background: var(--white); overflow: hidden;
    box-shadow: 0 14px 22px rgba(0,0,0,0.35);
    --main: var(--orange); --alt: var(--navy);
  }
  .flier--pest { left: 38px; }
  .flier--clean { left: 625px; --main: var(--navy); --alt: var(--orange); }

  .flier__brand {
    position: absolute; left: 22px; top: 22px; display: flex; align-items: center; gap: 8px;
    font-family: "Montserrat", sans-serif; font-weight: 700; font-size: 17px; color: var(--navy);
  }
  .flier__brand-mark { width: 30px; height: 30px; border-radius: 50%; background: var(--main); }
  .flier__brand small { display: block; font-size: 6px; font-weight: 600; color: var(--ink); letter-spacing: .3px; }

  .flier__title {
    position: absolute; top: 14px; right: 0; width: 304px; height: 62px;
    background: var(--main); clip-path: polygon(12px 0, 100% 0, 100% 100%, 0 100%);
    color: var(--white); font-family: "Montserrat", sans-serif; font-weight: 800; text-align: center;
    padding-left: 14px;
  }
  .flier__title-main { font-size: 31px; line-height: 34px; padding-top: 2px; letter-spacing: .3px; }
  .flier__title-sub { font-size: 20px; line-height: 22px; letter-spacing: 25px; margin-right: -25px; }

  .flier__hero { position: absolute; top: 78px; left: 0; width: 100%; height: 330px; }
  .flier--pest .flier__hero { background: linear-gradient(135deg, #e6e4e1 0%, #cfd0d3 40%, #3a57a8 60%, #dcdcdc 85%); }
  .flier--clean .flier__hero { background: linear-gradient(120deg, #d8d6d1 0%, #f2f1ee 35%, #a9b3a0 60%, #6f8aa4 80%, #c9d0d6 100%); }

  .flier__band {
    position: absolute; top: 317px; left: 0; width: 100%; height: 91px; background: var(--band);
    color: var(--white); text-align: center; font-family: "Montserrat", sans-serif; font-weight: 700;
    font-size: 14px; line-height: 19px; padding-top: 11px; border-bottom: 3px solid var(--main);
  }
  .flier__band .accent { color: var(--orange); }
  .flier--clean .flier__band { font-size: 14px; }
  .flier--clean .flier__band .accent { font-size: 17px; line-height: 20px; }

  .flier__pill {
    position: absolute; top: 390px; left: 20px; width: 206px; height: 32px; border-radius: 18px;
    background: var(--main); color: var(--white); font-family: "Montserrat", sans-serif;
    font-weight: 700; font-size: 21px; line-height: 32px; text-align: center;
    box-shadow: 0 2px 4px rgba(0,0,0,0.3);
  }

  .flier__services { position: absolute; top: 422px; left: 0; width: 100%; height: 122px; background: linear-gradient(90deg, #fafafa, var(--panel)); }
  .service-list { position: absolute; left: 24px; top: 21px; list-style: none; }
  .service-list li { display: flex; align-items: flex-start; gap: 12px; font-size: 15.5px; line-height: 20px; color: var(--ink); font-weight: 500; }
  .service-list svg { flex: none; margin-top: 3px; }
  .service-list .wrap { display: block; }
  .flier__divider { position: absolute; left: 234px; top: 20px; width: 1px; height: 88px; background: #bdbdbd; }
  .flier__pitch { position: absolute; left: 262px; top: 18px; width: 250px; }
  .flier__pitch-head { font-family: "Montserrat", sans-serif; font-weight: 700; font-size: 14.5px; line-height: 20px; color: var(--navy); }
  .flier__pitch-body { font-size: 10px; line-height: 13px; color: var(--ink); margin-top: 8px; }
  .flier--clean .flier__pitch { left: 252px; width: 262px; top: 24px; }
  .flier--clean .flier__pitch-head { color: var(--orange); font-size: 13px; line-height: 16px; }
  .flier--clean .flier__pitch-body { font-size: 8.6px; line-height: 11.7px; margin-top: 4px; }

  .flier__strip { position: absolute; top: 614px; left: 0; width: 100%; height: 62px; background: var(--alt); }
  .flier__thumb { position: absolute; top: 565px; width: 142px; height: 92px; border: 3px solid var(--white); box-shadow: 0 2px 5px rgba(0,0,0,0.35); }
  .flier__thumb--1 { left: 24px; } .flier__thumb--2 { left: 191px; } .flier__thumb--3 { left: 358px; }
  .flier--pest .flier__thumb--1 { background: linear-gradient(135deg, #f2f2f2, #d9c9a8 60%, #8a6a4a); }
  .flier--pest .flier__thumb--2 { background: linear-gradient(135deg, #3a3a3a, #b8b6ad 55%, #8a7a5a); }
  .flier--pest .flier__thumb--3 { background: linear-gradient(135deg, #ece8e2, #8a6d4f 50%, #d9b3a6); }
  .flier--clean .flier__thumb--1 { background: linear-gradient(135deg, #5a4a32, #e8c94a 55%, #2a2a2a); }
  .flier--clean .flier__thumb--2 { background: linear-gradient(135deg, #cfc9c4, #3c6fa8 50%, #e6d6cf); }
  .flier--clean .flier__thumb--3 { background: linear-gradient(135deg, #6c8a5a, #e9ecef 50%, #5aa0c8); }

  .flier__footer { position: absolute; bottom: 0; left: 0; width: 100%; height: 64px; background: var(--alt); }
  .flier__cta {
    position: absolute; left: 0; top: 0; width: 240px; height: 64px; background: var(--main);
    clip-path: polygon(0 0, 218px 0, 100% 100%, 0 100%); color: var(--white);
    font-family: "Montserrat", sans-serif; padding: 10px 0 0 22px;
  }
  .flier__cta-main { font-weight: 800; font-size: 24px; line-height: 24px; }
  .flier__cta-sub { font-weight: 500; font-size: 15px; line-height: 17px; }
  .flier__phone {
    position: absolute; right: 18px; top: 10px; display: flex; align-items: center; gap: 4px;
    color: var(--white); font-family: "Montserrat", sans-serif; font-weight: 800; font-size: 36px; line-height: 44px;
  }

  .flier-label { position: absolute; top: 790px; font-family: "Raleway", sans-serif; font-style: italic; font-size: 26px; color: #111; }
  .flier-label--pest { left: 478px; }
  .flier-label--clean { left: 1066px; }
</style>
</head>
<body>

<article class="flier flier--pest">
  <div class="flier__brand"><span class="flier__brand-mark"></span><span>QRV Pest Control</span></div>
  <div class="flier__title">
    <div class="flier__title-main">PEST CONTROL</div>
    <div class="flier__title-sub">SERVICE</div>
  </div>
  <div class="flier__hero" role="img" aria-label="Technician in blue overalls spraying along a kitchen skirting board"></div>
  <div class="flier__band">
    <div>EUROPEAN MANAGED</div>
    <div class="accent">MONTHLY - QUARTERLY - ANNUALLY MAINTENANCE CONTRACTS</div>
    <div>ON CALL SERVICE</div>
  </div>
  <div class="flier__pill">OUR SERVICES</div>
  <section class="flier__services">
    <ul class="service-list">
      <li><svg width="15" height="15" viewBox="0 0 16 16"><circle cx="8" cy="8" r="8" fill="#e98a1b"/><path d="M6.5 4.5 10 8l-3.5 3.5" stroke="#fff" stroke-width="2" fill="none"/></svg>General Pest Control</li>
      <li><svg width="15" height="15" viewBox="0 0 16 16"><circle cx="8" cy="8" r="8" fill="#e98a1b"/><path d="M6.5 4.5 10 8l-3.5 3.5" stroke="#fff" stroke-width="2" fill="none"/></svg>Bed Bugs Control</li>
      <li><svg width="15" height="15" viewBox="0 0 16 16"><circle cx="8" cy="8" r="8" fill="#e98a1b"/><path d="M6.5 4.5 10 8l-3.5 3.5" stroke="#fff" stroke-width="2" fill="none"/></svg>Rat Control</li>
      <li><svg width="15" height="15" viewBox="0 0 16 16"><circle cx="8" cy="8" r="8" fill="#e98a1b"/><path d="M6.5 4.5 10 8l-3.5 3.5" stroke="#fff" stroke-width="2" fill="none"/></svg>Cockroaches Control</li>
      <li><svg width="15" height="15" viewBox="0 0 16 16"><circle cx="8" cy="8" r="8" fill="#e98a1b"/><path d="M6.5 4.5 10 8l-3.5 3.5" stroke="#fff" stroke-width="2" fill="none"/></svg>Ant Control</li>
    </ul>
    <div class="flier__divider"></div>
    <div class="flier__pitch">
      <p class="flier__pitch-head">QRV Pest Control is reinventing the pest control service industry in Dubai.</p>
      <p class="flier__pitch-body">This means you get the right Pest Control Workers, with the right tools at the right time!</p>
    </div>
  </section>
  <div class="flier__strip"></div>
  <div class="flier__thumb flier__thumb--1" role="img" aria-label="Worker in protective suit spraying a floor"></div>
  <div class="flier__thumb flier__thumb--2" role="img" aria-label="Sprayer treating the base of an outside wall"></div>
  <div class="flier__thumb flier__thumb--3" role="img" aria-label="Technician inspecting a kitchen with the home owner"></div>
  <footer class="flier__footer">
    <div class="flier__cta"><div class="flier__cta-main">CALL US NOW</div><div class="flier__cta-sub">FOR A FREE ESTIMATE!</div></div>
    <div class="flier__phone"><svg width="14" height="30" viewBox="0 0 14 30"><path d="M11 2C5 2 3 8 3 15s2 13 8 13" stroke="#e98a1b" stroke-width="3" fill="none" stroke-linecap="round"/></svg>800 SPARKLE</div>
  </footer>
</article>
<div class="flier-label flier-label--pest">FRONT</div>

<article class="flier flier--clean">
  <div class="flier__brand"><span class="flier__brand-mark"></span><span>QRV<small>CENTER FOR DOMESTIC WORKERS SERVICES</small></span></div>
  <div class="flier__title">
    <div class="flier__title-main">HOME CLEANING</div>
    <div class="flier__title-sub">SERVICE</div>
  </div>
  <div class="flier__hero" role="img" aria-label="Bright living room with white sofas and a smiling housekeeper in uniform"></div>
  <div class="flier__band">
    <div>DOMESTIC HELPER ON LEAVE? NEED A PART-TIME CLEANER?</div>
    <div class="accent">CALL OUR MAIDS FOR HELP TODAY!</div>
    <div class="accent">THE BRIGHT HELP</div>
  </div>
  <div class="flier__pill">OUR SERVICES</div>
  <section class="flier__services">
    <ul class="service-list">
      <li><svg width="15" height="15" viewBox="0 0 16 16"><circle cx="8" cy="8" r="8" fill="#263d8c"/><path d="M6.5 4.5 10 8l-3.5 3.5" stroke="#fff" stroke-width="2" fill="none"/></svg>Same maid everytime</li>
      <li><svg width="15" height="15" viewBox="0 0 16 16"><circle cx="8" cy="8" r="8" fill="#263d8c"/><path d="M6.5 4.5 10 8l-3.5 3.5" stroke="#fff" stroke-width="2" fill="none"/></svg>Ironing</li>
      <li><svg width="15" height="15" viewBox="0 0 16 16"><circle cx="8" cy="8" r="8" fill="#263d8c"/><path d="M6.5 4.5 10 8l-3.5 3.5" stroke="#fff" stroke-width="2" fill="none"/></svg><span class="wrap">In-house training<br>facility</span></li>
      <li><svg width="15" height="15" viewBox="0 0 16 16"><circle cx="8" cy="8" r="8" fill="#263d8c"/><path d="M6.5 4.5 10 8l-3.5 3.5" stroke="#fff" stroke-width="2" fill="none"/></svg>Laundry</li>
    </ul>
    <div class="flier__divider"></div>
    <div class="flier__pitch">
      <p class="flier__pitch-head">PROFESSIONAL CLEANING SERVICE</p>
      <p class="flier__pitch-body">The Bright Help is one of the only cleaning companies to be offcially endorsed by the UAE government. This is because we look after our maids properly and have even built our own in house training facility to make sure that you only receive maids that are qualiffed to be in your home.</p>
    </div>
  </section>
  <div class="flier__strip"></div>
  <div class="flier__thumb flier__thumb--1" role="img" aria-label="Hand wiping a table with a yellow cloth"></div>
  <div class="flier__thumb flier__thumb--2" role="img" aria-label="Iron pressing a shirt"></div>
  <div class="flier__thumb flier__thumb--3" role="img" aria-label="Hand cleaning a window with a blue cloth"></div>
  <footer class="flier__footer">
    <div class="flier__cta"><div class="flier__cta-main">CALL US NOW</div><div class="flier__cta-sub">FOR A FREE ESTIMATE!</div></div>
    <div class="flier__phone"><svg width="14" height="30" viewBox="0 0 14 30"><path d="M11 2C5 2 3 8 3 15s2 13 8 13" stroke="#ffffff" stroke-width="3" fill="none" stroke-linecap="round"/></svg>800 SPARKLE</div>
  </footer>
</article>
<div class="flier-label flier-label--clean">FRONT</div>

</body>
</html>
```